I need a business card representing my company, VELDAR, it's an artist management and design company. Complete name is "VELDAR Artist Mgmt. + Design Co." I need it to be world class and very appealing, sophisticated and artistically unique.
Updates

Posted an updated Brief please see. I need a business card representing my company, VELDAR, it's an artist management and design company. Complete name is "VELDAR Artist Mgmt. + Design Co." I need it to be world class and very appealing, sophisticated and artistically unique.

Designs look the same

Designs look the same

Target Market(s)

Advertisers, Entertainment Companies, Commercial companies

Industry/Entity Type

Advertising

Contact Information for Business Card

I need a business card representing my company, VELDAR, it's an artist management and design company. Complete name is "VELDAR Artist Mgmt. + Design Co." I need it to be world class and very appealing, sophisticated and artistically unique. One side can be VELDAR Artist Mgmt. + Design Co. and the other my name, Theodore Quillan, my contact telephone: 415.638.2097, email veldarartist@mailnest.example, my address: 2416 Harrowgate Ave. #317 Miami, FL 33152

Font styles to use
Other font styles liked:
• Calibri

Colors
ffffff
0455a3
f37122

Requirements
Must have
• "VELDAR" stand out bigger than the rest of the text.
Nice to have
• Name "VELDAR" can be centered on one side or in the corner or along side edges, just need something cool and different.
Should not have
• I am open just try to keep it clean looking

```html
<!DOCTYPE html>
<html lang="en">
<head>
<meta charset="utf-8">
<title>VELDAR Business Card</title>
<link href="https://fonts.googleapis.com/css2?family=Open+Sans:wght@300;400;700&display=swap" rel="stylesheet">
<style>
  :root {
    --backdrop: #3b3c3e;
    --card: #ffffff;
    --ink: #000000;
    --ink-soft: #222222;
    --band: #000000;
    --band-text: #ffffff;
  }
  * { margin: 0; padding: 0; box-sizing: border-box; }
  html, body {
    width: 1200px; height: 1200px; overflow: hidden;
    background: var(--backdrop);
    font-family: "Open Sans", Calibri, sans-serif;
    color: var(--ink);
  }
  .canvas {
    position: relative; width: 1200px; height: 1200px;
  }
  .card {
    position: absolute; left: 180px;
    width: 840px; height: 480px;
    background: var(--card);
    border-radius: 44px;
    overflow: hidden;
    box-shadow: 0 14px 30px rgba(0,0,0,0.35);
  }
  .card--front { top: 90px; }
  .card--back { top: 630px; }

  .wordmark { position: absolute; line-height: 1; }
  .wordmark__name {
    display: block; font-weight: 700; letter-spacing: 1px;
  }
  .wordmark__tagline {
    display: block; font-weight: 400; color: var(--ink-soft);
  }
  .card--front .wordmark { left: 220px; top: 160px; }
  .card--front .wordmark__name { font-size: 112px; }
  .card--front .wordmark__tagline { font-size: 34px; margin-top: 4px; }

  .card--back .wordmark { left: 56px; top: 140px; }
  .card--back .wordmark__name { font-size: 86px; }
  .card--back .wordmark__tagline { font-size: 27px; margin-top: 2px; }

  .divider {
    position: absolute; left: 462px; top: 34px;
    width: 3px; height: 320px;
    background: linear-gradient(to bottom, rgba(0,0,0,0), rgba(0,0,0,0.85) 45%, rgba(0,0,0,0));
  }
  .contact { position: absolute; left: 500px; top: 86px; }
  .contact__name { font-size: 30px; font-weight: 700; margin-bottom: 34px; }
  .contact__row {
    display: flex; align-items: center; gap: 12px;
    font-size: 18px; font-weight: 300; margin-bottom: 14px;
  }
  .contact__icon { width: 22px; height: 22px; flex: none; }

  .address-band {
    position: absolute; left: 0; bottom: 0;
    width: 100%; height: 92px;
    background: var(--band); color: var(--band-text);
    display: flex; align-items: center; justify-content: center;
    font-size: 26px; font-weight: 700; letter-spacing: 0.3px;
  }
</style>
</head>
<body>
<main class="canvas">
  <section class="card card--front">
    <div class="wordmark">
      <span class="wordmark__name">VELDAR</span>
      <span class="wordmark__tagline">Artist Mgmt. + Design Co.</span>
    </div>
  </section>

  <section class="card card--back">
    <div class="wordmark">
      <span class="wordmark__name">VELDAR</span>
      <span class="wordmark__tagline">Artist Mgmt. + Design Co.</span>
    </div>
    <div class="divider"></div>
    <div class="contact">
      <p class="contact__name">Theodore Quillan</p>
      <p class="contact__row">
        <svg class="contact__icon" viewBox="0 0 22 22" aria-hidden="true">
          <rect x="1" y="1" width="20" height="20" rx="4" fill="none" stroke="#000" stroke-width="1.8"/>
          <path d="M7 5.5c-1 .8-1.3 2.2-.6 3.8 1 2.3 3 4.4 5.3 5.6 1.6.8 3 .5 3.9-.4l-2-2-1.4.9c-1.3-.6-2.4-1.7-3-3l.9-1.4z" fill="#000"/>
        </svg>
        415.638.2097
      </p>
      <p class="contact__row">
        <svg class="contact__icon" viewBox="0 0 22 22" aria-hidden="true">
          <rect x="1" y="1" width="20" height="20" rx="4" fill="none" stroke="#000" stroke-width="1.8"/>
          <rect x="5" y="6.5" width="12" height="9" fill="none" stroke="#000" stroke-width="1.5"/>
          <path d="M5 6.5l6 5 6-5M5 15.5l4.5-4.5M17 15.5l-4.5-4.5" fill="none" stroke="#000" stroke-width="1.3"/>
        </svg>
        veldarartist@mailnest.example
      </p>
    </div>
    <div class="address-band">2416 Harrowgate Ave. #317 Miami, FL 33152</div>
  </section>
</main>
</body>
</html>
```